Kelvo.cn needs pages to be re-designed

www.kelvo.cn is our current new site which was launched in April.
We're a financial services website in the crowdfunding space in China to connect borrower's and lender's.

test.kelvo.cn is our test site
u: test
p: fogpine
http://test.kelvo.cn/
http://test.kelvo.cn/user/accounts/new_lender
http://test.kelvo.cn/user/accounts/new_borrower
http://test.kelvo.cn/introductions/protection
http://test.kelvo.cn/introductions
http://test.kelvo.cn/introductions/kelvo_admin
http://test.kelvo.cn/introductions/contact
Some of the pages have pop-ups in the bloc's of the pages. Please click the links, to see more content.

User's currently criticize the website for being:
- Too Western looking
- Too simple, too little content
- Content NOT in the pop-ups are too simple
- Pictures are too big and too much blank space
- Relevant information is not there when needed
- The pictures are too generic

What we would like to do is re-design those pages with the same color scheme and style to be more compelling, efficient, non-intimidating and easy-to-use. Our audience is Ages 25-35 predominantly male investors.
We are looking for more ideas to make the content match the style, while bridging western and chinese design. Our ultimate goal is to increase registrants to the website and highlight our core competitive advantages.

Some competitors websites are:
www.tobumix.com
www.fesca.com
www.zwqvolt.com

Reason: Not enough good designs that follow the prompt. Same style, better information layout!

Reason: Still have not received a design we're satisfied with

Reason: WE DONT WANT A COMPLETE REDESIGN OF PAGES . KEEP THE EXACT SAME COLOR AND STYLE - WE WANT CONTENT RE-DESIGN! THE BLOCS ARE TOO SIMPLE - WE WANT MORE CONTENT INSIDE.

Reason: no new designs

Reason: no new designs

Reason: other non-registered pages need to be re-designed

```html
<!DOCTYPE html>
<html lang="en">
<head>
<meta charset="utf-8">
<title>Kelvo.cn – Home</title>
<link href="https://fonts.googleapis.com/css2?family=Fredoka:wght@500;600&family=Open+Sans:wght@400;600;700&display=swap" rel="stylesheet">
<style>
:root{
  --green:#4cb81e;
  --green-dark:#3a9a12;
  --navy:#1b1f3b;
  --text:#444;
  --muted:#8a8a8a;
  --line:#e2e2e2;
  --topbar:#2b2e35;
  --footer:#272b36;
  --footer-deep:#1d2029;
  --blue:#2a7db8;
  --band:#e7e8ea;
}
*{box-sizing:border-box;margin:0;padding:0}
html,body{width:829px;height:1200px;overflow:hidden;background:#fff}
body{position:relative;font-family:"Open Sans",Arial,sans-serif;color:var(--text)}
.abs{position:absolute}
.display{font-family:"Fredoka","Open Sans",sans-serif;font-weight:600;color:var(--navy)}

/* top bar */
.topbar{left:0;top:0;width:829px;height:27px;background:var(--topbar);color:#fff;font-size:10px}
.topbar .item{position:absolute;top:8px;display:flex;align-items:center;gap:4px}
.lang{position:absolute;left:692px;top:5px;width:38px;height:17px;border:1px solid #555;background:#222;display:flex;align-items:center;gap:6px;padding-left:5px}
.lang .box{width:13px;height:9px;background:#c9ccd4}

/* header */
.header{left:0;top:27px;width:829px;height:59px;background:linear-gradient(#f3f4f5,#e8eaec)}
.brand{position:absolute;left:97px;top:13px;display:flex;align-items:center;gap:8px}
.brand .mark{width:36px;height:36px;border-radius:50%;background:var(--green)}
.brand .name{font-family:"Fredoka",sans-serif;font-weight:600;font-size:20px;color:var(--navy)}
.nav{position:absolute;top:24px;font-size:9.5px;font-weight:600;color:#222;letter-spacing:.2px}
.nav.active{color:var(--green)}

/* hero */
.hero{left:0;top:86px;width:829px;height:225px;background:linear-gradient(90deg,#d9dbde 0%,#eceef0 30%,#c9ccd1 55%,#e4e6e9 75%,#cfd2d6 100%)}
.hero h1{position:absolute;left:455px;top:80px;font-size:27px;line-height:1}
.hero p{position:absolute;left:455px;top:114px;width:270px;font-family:"Fredoka",sans-serif;font-weight:500;font-size:14px;line-height:20px;color:var(--navy)}

/* features */
.feature{top:330px;width:190px}
.feature h3{display:flex;align-items:center;gap:8px;font-size:16px;margin-bottom:10px}
.feature .lead{font-size:9.5px;color:var(--muted);line-height:13px;margin-bottom:7px}
.feature .body{font-size:9.5px;color:#555;line-height:15px}
.feature a{display:block;font-size:8.5px;color:var(--green);text-decoration:none;margin-top:3px}
.vdivider{top:336px;width:1px;height:105px;background:linear-gradient(#fff,#e1e1e1,#fff)}

/* loan table */
.loans{left:97px;top:475px;width:634px;height:261px;border:1px solid #d9d9d9;border-radius:4px;overflow:hidden;box-shadow:0 2px 4px rgba(0,0,0,.06)}
.loans .head{height:35px;background:linear-gradient(#f7f7f7,#e9e9e9);border-bottom:1px solid #d5d5d5;position:relative}
.loans .head span{position:absolute;top:11px;font-family:"Fredoka",sans-serif;font-weight:500;font-size:12px;color:var(--navy)}
.row{height:35.5px;border-bottom:1px solid #ececec;position:relative;font-size:9px;color:#555}
.row:last-child{border-bottom:none}
.row.alt{background:#f6f6f6}
.row span{position:absolute;top:13px}
.row .c1{left:12px}.row .c3{left:232px}.row .c4{left:296px}.row .c5{left:393px}.row .pct{left:512px;font-size:8.5px}
.badges{position:absolute;left:136px;top:11px;display:flex;gap:3px}
.badge{width:12px;height:12px;border-radius:50%;background:var(--green);color:#fff;font-size:7px;font-weight:700;display:flex;align-items:center;justify-content:center}
.badge.blue{background:#5aa7e6}
.bar{position:absolute;left:467px;top:15px;width:40px;height:6px;background:#ccc;border-radius:3px;overflow:hidden}
.bar i{display:block;height:100%;background:var(--green)}
.btn{position:absolute;left:559px;top:11px;width:61px;height:14px;border-radius:7px;font-size:7px;color:#fff;display:flex;align-items:center;justify-content:center;background:var(--blue)}
.btn.full{background:#b3b3b3}

/* stats */
.stat{top:766px}
.stat .v{font-size:15px;line-height:1}
.stat .l{font-size:9px;color:#666;margin-top:6px}
.sdiv{top:756px;width:1px;height:52px;background:linear-gradient(#fff,#ddd,#fff)}
.invest{left:580px;top:769px;width:148px;height:30px;border-radius:15px;background:linear-gradient(#62cf2b,var(--green-dark));color:#fff;font-size:10.5px;font-weight:700;display:flex;align-items:center;justify-content:center;gap:8px;letter-spacing:.3px;box-shadow:0 0 0 2px #e8f6e0}

/* prepaid */
.prepaid-title{left:0;width:829px;top:851px;text-align:center;font-size:14px}
.bank{height:11px;width:54px;border-radius:2px}

/* partner band */
.partners{left:0;top:963px;width:829px;height:49px;background:var(--band)}
.partners .p{position:absolute;top:16px;height:17px;border-radius:2px;background:#c2c5ca}

/* footer */
.footer{left:0;top:1012px;width:829px;height:150px;background:linear-gradient(#2d3240,var(--footer))}
.flinks{position:absolute;top:27px;font-family:"Fredoka",sans-serif;font-weight:500;font-size:10px;color:#fff;line-height:19.5px;list-style:none}
.certs{position:absolute;left:343px;top:29px;width:177px;height:99px;background:#1b1d23;border:1px solid #3a3d45;border-radius:3px}
.certs i{position:absolute;height:18px;background:#c9cbcf;border-radius:1px}
.social{position:absolute;top:29px;width:26px;height:26px;background:#3a3e49;border-radius:2px}
.service{position:absolute;left:591px;top:64px;color:#fff;font-size:9.5px}
.service .on{color:var(--green)}
.service .tel{font-size:16px;font-weight:700;margin-top:3px;letter-spacing:.3px}
.service .hrs{font-size:9.5px;margin-top:2px}
.copy{left:0;top:1162px;width:829px;height:38px;background:var(--footer-deep);color:#8a8d96;font-size:9px;padding:16px 0 0 97px}
</style>
</head>
<body>

<div class="abs topbar">
  <span class="item" style="left:97px">
    <svg width="9" height="9" viewBox="0 0 10 10"><path d="M2 0.5 L4 2.8 L3 4 Q4.5 6 6 7 L7.2 6 L9.5 8 L8 9.5 Q3.5 9 0.5 2 Z" fill="#fff"/></svg>
    400 - 028 - 5570
  </span>
  <span class="item" style="left:189px">
    <svg width="10" height="8" viewBox="0 0 10 8"><rect x=".5" y=".5" width="9" height="7" fill="none" stroke="#fff"/><path d="M.5 .5 L5 4.5 L9.5 .5" fill="none" stroke="#fff"/></svg>
    contact@kelvo.cn
  </span>
  <span class="item" style="left:606px">Login</span>
  <span class="item" style="left:645px">Register</span>
  <div class="lang"><span class="box"></span><svg width="6" height="4" viewBox="0 0 6 4"><path d="M0 0H6L3 4Z" fill="#fff"/></svg></div>
</div>

<div class="abs header">
  <div class="brand"><span class="mark"></span><span class="name">Kelvo</span></div>
  <span class="nav active" style="left:509px">HOME</span>
  <span class="nav" style="left:558px">SECURITY</span>
  <span class="nav" style="left:621px">INVESTMENT</span>
  <span class="nav" style="left:698px">CREDIT</span>
</div>

<div class="abs hero">
  <div class="abs" role="img" aria-label="Photo of a smiling businesswoman in front of a blurred team of colleagues in an office" style="left:0;top:0;width:829px;height:225px"></div>
  <h1 class="display">Welcome to kelvo</h1>
  <p>Lorem Ipsum is simply dummy text of the printing and typesetting</p>
</div>

<div class="abs feature" style="left:97px">
  <h3 class="display">
    <svg width="18" height="16" viewBox="0 0 18 16"><rect x="1" y="9" width="4" height="7" fill="#f2a516"/><rect x="7" y="5" width="4" height="11" fill="#3b8fd4"/><rect x="13" y="1" width="4" height="15" fill="var(--green)"/></svg>
    High Returns</h3>
  <p class="lead">The annual rate of return of 10% -15%</p>
  <p class="body">Hope loan proceeds in a sustainable manner to maintain equilibrium.</p>
  <a href="#">Read More...</a>
</div>
<div class="abs vdivider" style="left:290px"></div>
<div class="abs feature" style="left:323px">
  <h3 class="display">
    <svg width="14" height="18" viewBox="0 0 14 18"><path d="M3 8V5a4 4 0 0 1 8 0v3" fill="none" stroke="#888" stroke-width="2"/><rect x="1" y="8" width="12" height="10" rx="1" fill="#999"/></svg>
    Security</h3>
  <p class="lead">The top priority of our work is to your financial security</p>
  <p class="body">We strive for a simple and secure financial management.</p>
  <a href="#">Read More...</a>
</div>
<div class="abs vdivider" style="left:527px"></div>
<div class="abs feature" style="left:565px">
  <h3 class="display">
    <svg width="18" height="18" viewBox="0 0 18 18"><circle cx="9" cy="9" r="8" fill="none" stroke="#888" stroke-width="2"/><circle cx="9" cy="9" r="3" fill="#888"/></svg>
    Efficient</h3>
  <p class="lead">Efficient service to your satisfaction</p>
  <p class="body">Get a loan within two days or three minutes to complete the investment.</p>
  <a href="#">Read More...</a>
</div>

<div class="abs loans">
  <div class="head">
    <span style="left:12px">The Title Lone</span>
    <span style="left:136px">Credit Rating</span>
    <span style="left:234px">ARP</span>
    <span style="left:296px">Amount</span>
    <span style="left:393px">Term</span>
    <span style="left:466px">Progress</span>
  </div>
  <div class="row"><span class="c1">Short-term liquidity</span><div class="badges"><i class="badge">A</i><i class="badge">✓</i></div><span class="c3">15.0%</span><span class="c4">50,000 yuan</span><span class="c5">12 Month</span><div class="bar"><i style="width:12%"></i></div><span class="pct">6.69%</span><span class="btn">Start lending</span></div>
  <div class="row"><span class="c1">Short-term liquidity</span><div class="badges"><i class="badge">A</i><i class="badge">✓</i><i class="badge blue">转</i></div><span class="c3">15.0%</span><span class="c4">8197.0 yuan</span><span class="c5">6 Month</span><div class="bar"><i style="width:22%"></i></div><span class="pct">9.23%</span><span class="btn">Start lending</span></div>
  <div class="row alt"><span class="c1">Business Loans</span><div class="badges"><i class="badge">S</i><i class="badge">✓</i><i class="badge blue">转</i></div><span class="c3">14.52%</span><span class="c4">12,782.0 yuan</span><span class="c5">9 Month</span><div class="bar"><i style="width:70%"></i></div><span class="pct">61.25%</span><span class="btn">Start lending</span></div>
  <div class="row"><span class="c1">Short-term liquidity</span><div class="badges"><i class="badge">A</i><i class="badge">✓</i></div><span class="c3">15.0%</span><span class="c4">50,000 yuan</span><span class="c5">12 Month</span><div class="bar"><i style="width:100%"></i></div><span class="pct">100.0%</span><span class="btn full">Full scal</span></div>
  <div class="row"><span class="c1">Expand business</span><div class="badges"><i class="badge">A</i><i class="badge">✓</i></div><span class="c3">15.0%</span><span class="c4">40,000 yuan</span><span class="c5">12 Month</span><div class="bar"><i style="width:100%"></i></div><span class="pct">100.0%</span><span class="btn full">Full scal</span></div>
  <div class="row"><span class="c1">Cash flow</span><div class="badges"><i class="badge">A</i><i class="badge">✓</i></div><span class="c3">15.0%</span><span class="c4">50,000 yuan</span><span class="c5">12 Month</span><div class="bar"><i style="width:100%"></i></div><span class="pct">100.0%</span><span class="btn full">Full scal</span></div>
</div>

<div class="abs stat" style="left:105px"><div class="v display">¥ 160407</div><div class="l">Funding needs</div></div>
<div class="abs sdiv" style="left:212px"></div>
<div class="abs stat" style="left:249px"><div class="v display">14.69%</div><div class="l">Average yield</div></div>
<div class="abs sdiv" style="left:343px"></div>
<div class="abs stat" style="left:376px"><div class="v display">12.24 month</div><div class="l">The average duration of</div></div>
<svg class="abs" style="left:492px;top:770px" width="84" height="26" viewBox="0 0 84 26"><path d="M2 24 Q10 4 40 6 Q62 7 76 10" fill="none" stroke="#222" stroke-width="1.3"/><path d="M70 5 L78 10 L70 14" fill="none" stroke="#222" stroke-width="1.3"/></svg>
<div class="abs invest">START INVESTING
  <svg width="11" height="11" viewBox="0 0 11 11"><path d="M0 3.5H5V0L11 5.5 5 11V7.5H0Z" fill="#fff"/></svg>
</div>

<div class="abs prepaid-title display">Prepaid Account</div>
<svg class="abs" style="left:95px;top:894px" width="16" height="24" viewBox="0 0 16 24"><path d="M13 2 L3 12 L13 22" fill="none" stroke="#ccc" stroke-width="3"/></svg>
<svg class="abs" style="left:716px;top:894px" width="16" height="24" viewBox="0 0 16 24"><path d="M3 2 L13 12 L3 22" fill="none" stroke="#ccc" stroke-width="3"/></svg>
<div class="abs bank" style="left:195px;top:889px;background:#bfd9cf"></div>
<div class="abs bank" style="left:268px;top:889px;background:#e6bcbc"></div>
<div class="abs bank" style="left:342px;top:889px;background:#bccbe0"></div>
<div class="abs bank" style="left:416px;top:889px;background:#ead9b5"></div>
<div class="abs bank" style="left:487px;top:889px;background:#e6bcbc"></div>
<div class="abs bank" style="left:561px;top:889px;background:#e6bcbc"></div>
<div class="abs bank" style="left:195px;top:912px;background:#e6bcbc"></div>
<div class="abs bank" style="left:268px;top:912px;background:#e6bcbc"></div>
<div class="abs bank" style="left:342px;top:912px;background:#bccbe0"></div>
<div class="abs bank" style="left:416px;top:912px;background:#bccbe0"></div>
<div class="abs bank" style="left:487px;top:912px;background:#bfd9cf"></div>
<div class="abs bank" style="left:561px;top:912px;background:#e6bcbc"></div>

<div class="abs partners">
  <i class="p" style="left:97px;width:76px"></i>
  <i class="p" style="left:211px;width:104px"></i>
  <i class="p" style="left:336px;width:126px"></i>
  <i class="p" style="left:489px;width:28px;height:20px;top:14px"></i>
  <i class="p" style="left:543px;width:53px;height:20px;top:14px"></i>
  <i class="p" style="left:622px;width:106px"></i>
</div>

<div class="abs footer">
  <ul class="flinks" style="left:97px"><li>About Us</li><li>Contact us</li><li>Join us</li><li>Help Center</li><li>Net lone home</li></ul>
  <ul class="flinks" style="left:187px"><li>Investment</li><li>Security</li><li>Media</li><li>Cooperation</li><li>Net lone eye in the sky</li></ul>
  <div class="certs">
    <i style="left:13px;top:11px;width:68px"></i>
    <i style="left:95px;top:11px;width:70px"></i>
    <i style="left:13px;top:40px;width:95px"></i>
    <i style="left:114px;top:40px;width:22px"></i>
    <i style="left:13px;top:69px;width:68px"></i>
    <i style="left:88px;top:69px;width:72px"></i>
  </div>
  <i class="social" style="left:591px"></i>
  <i class="social" style="left:628px"></i>
  <i class="social" style="left:666px"></i>
  <i class="social" style="left:703px"></i>
  <div class="service">
    <div class="on">Online Services</div>
    <div style="margin-top:5px">Customer Service Phone</div>
    <div class="tel">400 - 028 - 5570</div>
    <div class="hrs">Monday to Friday, 9:00 - 18:00</div>
  </div>
</div>

<div class="abs copy">Copyright © 2014 kelvo.cn</div>

</body>
</html>
```